Company letter head and business card for new Indian Pharmaceutical Export company.

We need a letterhead and business card design for an Indian Pharmaceutical Export company.

The letter head needs to contain the following information.
Vorin Healthline Pvt. Ltd.
Office No 4827 Plot No 19, Larkspire, KT Lane, 400153, Maharashtra, India.
Email: info@vorin-healthline.com
Phone: +91-8342196507
CIN: U71853MH2025PTC902617
GSTIN: (This number is still pending, we will add later)

The business card needs to contain:
Address:
Vorin Healthline Pvt. Ltd.
Office No 4827 Plot No19, Larkspire, KT Lane, 400153, MH, India.
Email: torvald@vorin-healthline.com
Phone: +49-17634902851
Name on card: Torvald Ramming
Position: Director

The design for the letter head and business card should be simple but trustworthy.
Please use only Green and blue, same as in the attached logo.

```html
<!DOCTYPE html>
<html lang="en">
<head>
<meta charset="utf-8">
<title>Vorin Healthline Letterhead</title>
<link rel="stylesheet" href="https://fonts.googleapis.com/css2?family=Montserrat:wght@500;700&family=Arimo:wght@400&display=swap">
<style>
  :root {
    --blue: #1a5ea8;
    --blue-deep: #15579e;
    --green: #7cc242;
    --ink: #1d1d1f;
    --muted: #3b3b3b;
    --backdrop: #e9e9eb;
    --paper: #ffffff;
  }
  * { box-sizing: border-box; margin: 0; padding: 0; }
  html, body { width: 1200px; height: 874px; overflow: hidden; background: var(--backdrop); }
  .letterhead {
    position: absolute; left: 310px; top: 27px; width: 580px; height: 820px;
    background: var(--paper); box-shadow: 0 4px 18px rgba(0,0,0,.12);
    font-family: "Arimo", Arial, sans-serif; color: var(--ink); overflow: hidden;
  }
  .brand {
    position: absolute; left: 40px; top: 46px; display: flex; align-items: center; gap: 8px;
    font-family: "Montserrat", sans-serif; font-weight: 700; font-size: 15px; color: var(--blue);
  }
  .brand-dot { width: 14px; height: 14px; border-radius: 50%; background: var(--green); }
  .header-info { position: absolute; right: 36px; top: 40px; display: flex; gap: 10px; align-items: stretch; }
  .company-address { text-align: right; font-family: "Montserrat", sans-serif; font-size: 7.5px; line-height: 1.45; color: var(--muted); font-weight: 500; }
  .company-name { color: var(--blue); font-size: 9px; font-weight: 700; }
  .divider { width: 1px; background: var(--green); }
  .contacts { list-style: none; font-family: "Montserrat", sans-serif; font-size: 7.5px; line-height: 1.55; color: var(--muted); font-weight: 500; }
  .contacts li { display: flex; align-items: center; gap: 5px; }
  .contacts svg { width: 7px; height: 7px; fill: var(--green); }
  .watermark {
    position: absolute; left: 150px; top: 240px; width: 300px; height: 300px; border-radius: 50%;
    border: 22px solid rgba(26,94,168,.05);
  }
  .recipient { position: absolute; left: 58px; top: 165px; font-size: 9.5px; line-height: 1.45; }
  .body { position: absolute; left: 58px; right: 58px; top: 240px; font-size: 9.5px; line-height: 1.5; }
  .body p { margin-bottom: 14px; }
  .closing { margin-top: 6px; }
  .signature { width: 120px; height: 40px; margin-top: 10px; background: linear-gradient(90deg, rgba(0,0,0,.08), rgba(0,0,0,.02)); border-radius: 3px; }
  .footer { position: absolute; left: 0; bottom: 0; width: 580px; height: 70px; }
  .registration {
    position: absolute; left: 360px; bottom: 16px; color: #fff; font-family: "Montserrat", sans-serif;
    font-size: 8px; font-weight: 500; letter-spacing: .2px; white-space: nowrap;
  }
  .registration .sep { color: var(--green); margin: 0 5px; }
</style>
</head>
<body>
<main class="letterhead">
  <div class="brand"><span class="brand-dot"></span>Vorin Healthline</div>

  <header class="header-info">
    <div class="company-address">
      <div class="company-name">Vorin Healthline Pvt. Ltd.</div>
      <div>Office No 4827 Plot No 19, Larkspire, KT Lane</div>
      <div>400153, Mumbai, Maharashtra, India</div>
    </div>
    <div class="divider"></div>
    <ul class="contacts">
      <li><svg viewBox="0 0 10 10"><path d="M2 0l2 2.5-1 1.2c.6 1.3 1.6 2.3 2.8 2.9L7 5.6 10 7.5 8.8 10C4 9.6.3 6 0 1.2z"/></svg>+91-8342196507</li>
      <li><svg viewBox="0 0 10 10"><path d="M0 2h10v6H0z"/></svg>info@vorin-healthline.com</li>
      <li><svg viewBox="0 0 10 10"><circle cx="5" cy="5" r="5"/></svg>www.vorin-healthline.com</li>
    </ul>
  </header>

  <div class="watermark" aria-hidden="true"></div>

  <section class="recipient">
    <div>Mr/s</div>
    <div>First Name and Last Name</div>
    <div>Company Name</div>
    <div>Address</div>
  </section>

  <section class="body">
    <p>Lorem Ipsum is simply dummy text of the printing and typesetting industry. Lorem Ipsum has been the industry's standard dummy text ever since the 1500s, when an unknown printer took a galley of type and scrambled it to make a type specimen book. It has survived not only five centuries, but also the leap into electronic typesetting, remaining essentially unchanged. It was popularised in the 1960s with the release of Letraset sheets containing Lorem Ipsum passages.</p>
    <p>The standard chunk of Lorem Ipsum used since the 1500s is reproduced below for those interested. Sections 1.10.32 and 1.10.33 from "de Finibus Bonorum et Malorum" by Cicero are also reproduced in their exact original form, accompanied by English versions from the 1914 translation by H. Rackham. Lorem ipsum dolor sit amet, consectetur adipiscing elit, sed do eiusmod tempor incididunt ut labore et dolore magna aliqua.</p>
    <p>It is a long established fact that a reader will be distracted by the readable content of a page when looking at its layout. The point of using Lorem Ipsum is that it has a more-or-less normal distribution of letters, as opposed to using 'Content here, content here', making it look like readable English. Many desktop publishing packages and web page editors now.</p>
    <div class="closing">Your Sincerely,</div>
    <div class="signature" role="img" aria-label="Handwritten signature"></div>
  </section>

  <footer class="footer">
    <svg width="580" height="70" viewBox="0 0 580 70" aria-hidden="true">
      <path d="M0 54 H290 C308 54 312 26 330 26 H580" fill="none" stroke="var(--green)" stroke-width="2.5"/>
      <path d="M0 60 H296 C314 60 318 32 336 32 H580 V70 H0 Z" fill="var(--blue-deep)"/>
    </svg>
    <div class="registration">CIN: U71853MH2025PTC902617<span class="sep">|</span>GSTIN: Pending</div>
  </footer>
</main>
</body>
</html>
```